Tour Guide in Israel business card

I am a tour guide in Israel (the holy land). Prior to it I have over 20 years high-tech business. My main (but not only) focus is working with business people that come to Israel and want to get a tour (usually short from few hours to 2 days). During my guiding I incorporate a lot of my know how of the Israeli business culture. I like to have a business card that I can present to anyone that is looking for a tour guide, but that business people will understand the additional value I can provide them during my tour.

Target Market(s)

Business visitors and tourist to Israel

Industry/Entity Type

Tourism

Contact Information for Business Card

Dorian Kaplow
email: dorian@kaplowtours.net
Mobile: +972-52-7186450

Colors

Designer to choose colors to be used in the design.

Requirements
Must have
• Tour Guide
Nice to have
• I don't know how but it should project my understanding in business not just the tourist side of my knowledge.

```html
<!DOCTYPE html>
<html lang="en">
<head>
<meta charset="utf-8">
<title>Dorian Kaplow — Tour Guide in Israel business card</title>
<link rel="stylesheet" href="https://fonts.googleapis.com/css2?family=Cormorant+Garamond:wght@400;500&family=Dancing+Script:wght@500;600&display=swap">
<style>
  :root {
    --canvas: #d9d9d9;
    --card: #ffffff;
    --ink: #0b0b0b;
    --line: #ffffff;
    --text-light: #f5f5f5;
    --shadow: rgba(0, 0, 0, 0.18);
  }
  * { box-sizing: border-box; margin: 0; padding: 0; }
  html, body {
    width: 1200px;
    height: 1200px;
    overflow: hidden;
    background: var(--canvas);
  }
  .sheet {
    width: 1200px;
    height: 1200px;
    display: flex;
    flex-direction: column;
    align-items: center;
    justify-content: center;
    gap: 70px;
  }
  .card {
    position: relative;
    width: 840px;
    height: 480px;
    background: var(--card);
    box-shadow: 0 6px 20px var(--shadow);
  }

  /* Logo side */
  .card--brand .panel {
    position: absolute;
    left: 150px; right: 150px;
    top: 75px; bottom: 75px;
    background: var(--ink);
  }
  .card--brand .panel::after {
    content: "";
    position: absolute;
    inset: 12px;
    border: 2px solid var(--line);
  }
  .brand {
    position: absolute;
    inset: 0;
    display: flex;
    flex-direction: column;
    align-items: center;
    justify-content: center;
    color: var(--text-light);
    font-family: "Dancing Script", cursive;
  }
  .brand__name {
    font-size: 62px;
    font-weight: 500;
    line-height: 1.1;
  }
  .brand__tagline {
    font-size: 22px;
    font-weight: 500;
    margin-top: 6px;
  }

  /* Contact side */
  .card--contact .panel {
    position: absolute;
    inset: 28px;
    background: var(--ink);
  }
  .card--contact .panel::after {
    content: "";
    position: absolute;
    inset: 14px;
    border: 2px solid var(--line);
  }
  .contact {
    position: absolute;
    inset: 0;
    display: flex;
    flex-direction: column;
    align-items: center;
    padding-top: 78px;
    color: var(--text-light);
    text-align: center;
  }
  .contact__name {
    font-family: "Cormorant Garamond", serif;
    font-weight: 500;
    font-size: 40px;
    letter-spacing: 2px;
    margin-bottom: 26px;
  }
  .contact__line {
    font-family: "Cormorant Garamond", serif;
    font-size: 28px;
    line-height: 1.3;
    letter-spacing: 0.5px;
  }
  .contact__tagline {
    font-family: "Dancing Script", cursive;
    font-weight: 600;
    font-size: 50px;
    margin-top: 34px;
  }
</style>
</head>
<body>
  <main class="sheet">
    <section class="card card--brand" aria-label="Business card, front">
      <div class="panel">
        <div class="brand">
          <h1 class="brand__name">Dorian Kaplow</h1>
          <p class="brand__tagline">Tour Guide In Israel</p>
        </div>
      </div>
    </section>

    <section class="card card--contact" aria-label="Business card, back">
      <div class="panel">
        <div class="contact">
          <h2 class="contact__name">DORIAN KAPLOW</h2>
          <p class="contact__line">+ 972-52-7186450</p>
          <p class="contact__line">dorian@kaplowtours.net</p>
          <p class="contact__tagline">tour guide in Israel (the holy land)</p>
        </div>
      </div>
    </section>
  </main>
</body>
</html>
```